Wedding Vow Design for Modern Print - SUBWAY PRINT STYLE or Similar, MODERN

I recently got married and I want to take the main words from my wedding vows and create a design using them that I can have printed and present to my new wife. I told her that I had privileges with Marring her and I made her promises. I would like to highlight both. We have a modern home and I want something that we can have professionally framed and hung on the wall. Love modern and clean design but something interesting.

Target Market(s)

Myself. 35, modern and loves clean design.

Industry/Entity Type

Wedding

Font styles to use
Serif

Colors
f6f3f8
ffffff
fbd4d5
000000
9d9d9d
dddddd

Requirements
Must have
• Cool, clean and modern design. Neutral Colors, Clean lines, Black and White, no reds, pinks, etc.
• We will hang this in our California modern home.
Nice to have
• Our wedding colors were , Gray,Black, Light Pink. I love the Subway signs and also love Black and White Word art.
Should not have
• Flowers, squiggly lines, traditional design. Something that would look great in a stainless metal frame or mirrored frame on white walls.

```html
<!DOCTYPE html>
<html lang="en">
<head>
<meta charset="utf-8">
<title>Our Vows – Privileges &amp; Promises</title>
<link rel="stylesheet" href="https://fonts.googleapis.com/css2?family=Graduate&family=Alfa+Slab+One&family=Rubik:wght@800&family=IBM+Plex+Sans:wght@300&family=Glegoo&display=swap">
<style>
  :root{
    --paper:#f6f3f8;
    --white:#ffffff;
    --blush:#fbd4d5;
    --ink:#000000;
    --stone:#9d9d9d;
    --mist:#dddddd;
  }
  *{margin:0;padding:0;box-sizing:border-box}
  html,body{width:1200px;height:960px;overflow:hidden;background:var(--ink)}
  .print{position:relative;width:1200px;height:960px;background:var(--ink)}
  .mat{position:absolute;left:16px;top:16px;width:1168px;height:928px;background:var(--paper)}
  .board{position:absolute;left:90px;top:72px;width:1020px;height:816px;background:var(--ink)}
  .title{
    position:absolute;left:0;top:104px;width:1200px;text-align:center;
    font-family:"Graduate",serif;font-size:118px;line-height:1;color:var(--blush);
    -webkit-text-stroke:3px var(--white);paint-order:stroke fill;letter-spacing:2px;
  }
  .banner{position:absolute;left:0;top:0}
  .banner-label{
    position:absolute;top:258px;font-family:"Alfa Slab One",serif;font-size:31px;
    color:var(--stone);letter-spacing:2px;line-height:1;
  }
  .banner-label--privileges{right:678px}
  .banner-label--promises{left:668px}
  .seal{
    position:absolute;left:546px;top:228px;width:104px;height:104px;border-radius:50%;
    background:radial-gradient(circle,var(--blush) 0 46%,var(--white) 47% 58%,var(--stone) 60% 100%);
  }
  .vow{position:absolute;font-size:33px;line-height:1;white-space:nowrap}
  .privileges .vow{right:628px;text-align:right}
  .promises .vow{left:628px}
  .vow--bold{font-family:"Rubik",sans-serif;font-weight:800;letter-spacing:1.5px;color:var(--white)}
  .vow--stone{color:var(--mist)}
  .vow--light{font-family:"IBM Plex Sans",sans-serif;font-weight:300;letter-spacing:1px;color:var(--white)}
  .vow--slab{font-family:"Glegoo",serif;color:var(--white);letter-spacing:.5px}
  .vow--blush{color:var(--blush)}
  .times{
    display:inline-block;width:20px;height:20px;border-radius:50%;background:var(--blush);
    color:var(--ink);font-size:17px;line-height:19px;text-align:center;vertical-align:3px;margin:0 6px;
    font-family:"IBM Plex Sans",sans-serif;font-weight:300;
  }
  .closing{
    position:absolute;left:0;top:742px;width:1200px;text-align:center;
    font-family:"Alfa Slab One",serif;font-size:33px;line-height:40px;color:var(--ink);letter-spacing:2.5px;
  }
</style>
</head>
<body>
<main class="print">
  <div class="mat"></div>
  <div class="board"></div>

  <h1 class="title">OUR VOWS</h1>

  <svg class="banner" width="1200" height="960" viewBox="0 0 1200 960" aria-hidden="true">
    <polygon points="253,253 945,253 910,279 945,306 253,306 288,279" fill="var(--blush)"/>
    <polygon points="367,727 833,727 815,782 833,838 367,838 385,782" fill="var(--blush)"/>
    <rect x="385" y="727" width="430" height="111" fill="var(--mist)"/>
  </svg>

  <span class="banner-label banner-label--privileges">PRIVILEGES</span>
  <div class="seal" role="img" aria-label="Round scalloped seal with a small bride and groom emblem"></div>
  <span class="banner-label banner-label--promises">PROMISES</span>

  <section class="privileges">
    <p class="vow vow--bold vow--stone" style="top:369px">REST OF MY LIFE</p>
    <p class="vow vow--slab" style="top:414px">Protection</p>
    <p class="vow vow--light" style="top:460px">PROVISION</p>
    <p class="vow vow--bold" style="top:522px">LOVE<span class="times">×</span>REGARDLESS</p>
    <p class="vow vow--light" style="top:568px">CARE</p>
    <p class="vow vow--slab" style="top:614px">Purpose</p>
    <p class="vow vow--bold" style="top:676px">PATIENCE</p>
  </section>

  <section class="promises">
    <p class="vow vow--light" style="top:369px">FIGHT</p>
    <p class="vow vow--slab" style="top:414px">Safety</p>
    <p class="vow vow--bold vow--blush" style="top:476px">CHERISH</p>
    <p class="vow vow--slab" style="top:522px">Unconditional Support</p>
    <p class="vow vow--light" style="top:568px">LISTEN</p>
    <p class="vow vow--bold vow--stone" style="top:630px">BY YOUR SIDE</p>
  </section>

  <p class="closing">THE BEST IN YOU<br>THE BEST IN ME</p>
</main>
</body>
</html>
```